KESTREL RIDGE SPORTS AVIATION CLUB

WE MAKE FLYING FUN AGAIN! We are a Semi Government Sport Aviation club that focuses on the highest quality of aviation training but in the spirit of Sport flying. The club is for aviation enthusiasts to come and share their passion with other club members to build their sport pilot skills.
Club Background and Structure: Club is Semi-Government and falls under the Marlowe Vale Sports Council. We have seven Board Members that Shape the vision of the club. We have a CEO that take care of KRSAC as a whole and an Operations Manager that takes charge of Daily Flight Operations.
SPORT FLYING is different from a normal Pilots license due to the fact that the pilots fly as a hobby and fun and NOT for Commercial purposes . We would like a design to represent a professional but yet fun side of flying to showcase the "club" side (pilot family)
The club focuses on 3 types of Aircraft Fixed wing aircraft, Gyrocopters and Paramotor (NOTE: Paramotor will have their own web page, but the paramotor must be featured as one of the options. when the pilot chooses the paramotor it must link to paramotor web page)
The page must have the following MINIMUM requirements:
1. General page with logo and some nice pictures that feature both aircraft types (photos in files section)
2. "Get Started" tab that features the following sequence a: Choose your aircraft ( picture of Fixed wing and picture of gyrocopter and picture of paramotor)
b: Get a Introductory Flight.
2. "About us"
3. Services & Price
4. Our Team
5. Fleet
6. Bookings (pilots and introductory scenic flights)
7. Events (with calendar please)
8. Contact us
9. FAQ
10 Ground School
11 Other Sports and Activities
12 Our Partners

Requirements
Must have
• Professional design and easy to maintain and user friendlyness
Nice to have
• We have a booking system that needs to be connected to web page if possible
Should not have
• no clip art

```html
<!DOCTYPE html>
<html lang="en">
<head>
<meta charset="utf-8">
<title>KRSAC — Kestrel Ridge Sports Aviation Club</title>
<link rel="stylesheet" href="https://fonts.googleapis.com/css2?family=Poppins:wght@400;500;600;700;800&display=swap">
<style>
:root{
  --magenta:#c4168d;
  --purple:#7a3da3;
  --teal:#2a93b8;
  --teal-light:#3fb2d8;
  --navy:#14265c;
  --navy-deep:#0f1d4a;
  --grey-band:#e7e7ea;
  --text:#2a2a2a;
  --footer:#1b1c22;
  --grad:linear-gradient(90deg,var(--magenta),var(--purple));
}
*{box-sizing:border-box;margin:0;padding:0}
html,body{width:1200px;height:4120px;overflow:hidden}
body{position:relative;font-family:"Poppins",sans-serif;color:var(--text);background:#fff}
.abs{position:absolute}
.grad-text{background:var(--grad);-webkit-background-clip:text;background-clip:text;color:transparent}

/* nav */
.nav{top:0;left:0;width:1200px;height:59px;background:linear-gradient(90deg,#2c3f9a,#5b3aa0 60%,#8a3b9e);z-index:3}
.nav a{position:absolute;top:0;height:59px;line-height:59px;color:#fff;font-size:14px;font-weight:500;text-decoration:none}
.nav .active{background:var(--magenta);padding:0 16px}
.book-now{position:absolute;left:1006px;top:19px;width:106px;height:32px;border:1.5px solid #fff;border-radius:3px;color:#fff;font-size:13px;font-weight:500;text-align:center;line-height:29px}

/* hero */
.hero{top:0;left:0;width:1200px;height:523px;
  background:
    radial-gradient(ellipse 150px 90px at 230px 150px,rgba(222,178,120,.95),rgba(222,178,120,0) 100%),
    radial-gradient(ellipse 90px 60px at 250px 420px,rgba(70,50,40,.55),rgba(70,50,40,0) 100%),
    radial-gradient(ellipse 190px 110px at 1010px 400px,rgba(242,190,40,.95),rgba(242,190,40,0) 100%),
    radial-gradient(ellipse 330px 200px at 620px 270px,rgba(255,255,255,.85),rgba(255,255,255,0) 100%),
    linear-gradient(180deg,#2f7fcb 0%,#79b3e4 40%,#cfd9e2 68%,#dcbd94 86%,#c39264 100%)}
.hero-brand{left:440px;top:228px;width:400px;text-align:center}
.hero-brand .mark{font-size:66px;font-weight:800;color:var(--teal);letter-spacing:2px;line-height:1}
.hero-brand .full{font-size:15px;font-weight:600;color:var(--navy);letter-spacing:.5px;margin-top:14px;white-space:nowrap}
.dot{top:484px;width:14px;height:14px;border:2px solid #fff;border-radius:50%}

/* about */
.about-photo{left:141px;top:603px;width:403px;height:293px;clip-path:polygon(0 0,77% 0,100% 100%,23% 100%);
  background:
    radial-gradient(circle 70px at 150px 80px,rgba(240,240,240,.95),rgba(240,240,240,0)),
    radial-gradient(circle 80px at 300px 140px,rgba(225,225,225,.9),rgba(225,225,225,0)),
    radial-gradient(ellipse 110px 80px at 180px 250px,rgba(240,200,40,.95),rgba(240,200,40,0)),
    radial-gradient(ellipse 120px 90px at 110px 190px,rgba(210,50,50,.9),rgba(210,50,50,0)),
    linear-gradient(135deg,#8a9a9e,#c9b8a4 40%,#6a6f72)}
.about-title{left:584px;top:648px;font-size:38px;font-weight:700}
.about-sub{left:584px;top:709px;font-size:14px;font-weight:600;color:var(--teal)}
.about-text{left:584px;top:738px;width:470px;font-size:13.5px;line-height:20px;color:#333}
.btn-outline{border:2px solid var(--magenta);border-radius:3px;color:var(--teal);font-size:13.5px;font-weight:500;text-align:center}

/* aircraft */
.aircraft{top:976px;left:0;width:1200px;height:669px;
  background:
    radial-gradient(ellipse 500px 200px at 200px 560px,rgba(80,110,160,.35),rgba(80,110,160,0)),
    radial-gradient(ellipse 500px 200px at 1000px 120px,rgba(80,110,160,.3),rgba(80,110,160,0)),
    linear-gradient(180deg,#1b2f68,#13245a 60%,#0f1f4e)}
.section-title{width:1200px;left:0;text-align:center;font-weight:800;text-transform:uppercase}
.card{top:1174px;width:320px;height:303px;background:#fff;border:2px solid #fff}
.card .photo{height:238px}
.card .label{height:61px;line-height:61px;text-align:center;font-size:21px;font-weight:600;color:#222}
.card.selected .label{background:linear-gradient(90deg,var(--magenta),#8c3aa3 60%,var(--teal));color:#fff}

/* services */
.svc{top:1830px;width:182px;height:149px;background:var(--teal);color:#fff;text-align:center}
.svc.selected{background:linear-gradient(90deg,var(--magenta),var(--purple))}
.svc .icon{position:absolute;left:63px;top:24px;width:56px;height:56px}
.svc .name{position:absolute;left:0;width:100%;top:94px;font-size:17px;font-weight:500}
.svc .toggle{position:absolute;left:71px;bottom:-20px;width:40px;height:40px;border-radius:50%;background:var(--teal);border:3px solid #fff}
.svc.selected .toggle{background:linear-gradient(90deg,var(--magenta),var(--purple))}

/* team */
.team{top:2080px;left:0;width:1200px;height:554px;background:var(--grey-band)}
.member{top:2227px;width:221px;height:224px;border:2px solid #fff}
.member-name{top:2466px;width:221px;text-align:center;font-size:15px;color:#222}
.btn-solid{background:var(--grad);color:#fff;font-size:13.5px;font-weight:500;text-align:center;border-radius:2px}

/* events */
.events{top:2634px;left:0;width:1200px;height:742px;background:linear-gradient(180deg,#15286a,#112160)}
.ev-img{left:179px;width:240px;height:96px}
.ev-date{left:157px;width:56px;height:67px;background:var(--teal);color:#fff;text-align:center;padding-top:9px}
.ev-date b{display:block;font-size:20px;line-height:22px}
.ev-date span{font-size:13px}
.ev-title{left:443px;font-size:19px;color:var(--teal-light);font-weight:500}
.ev-desc{left:443px;width:430px;font-size:11.5px;line-height:18px;color:#e6e8f2}
.ev-btn{left:914px;width:129px;height:36px;line-height:32px;border:2px solid var(--magenta);border-radius:2px;text-align:center;font-size:13.5px;color:var(--teal-light)}
.ev-btn.active{background:var(--magenta);color:#fff}

/* partners */
.partner{top:3566px;width:150px;height:80px}
.vsep{top:3560px;width:1px;height:95px;background:#e2e2e6}
.arrow-btn{top:3587px;width:38px;height:38px;border-radius:50%}

/* footer */
.footer{top:3734px;left:0;width:1200px;height:343px;
  background:
    radial-gradient(ellipse 400px 200px at 300px 250px,rgba(70,72,85,.45),rgba(70,72,85,0)),
    linear-gradient(180deg,#202128,#17181d)}
.foot-head{font-size:16px;font-weight:600;color:var(--magenta)}
.foot-link{font-size:13px;color:#fff}
.copyright{top:4077px;left:0;width:1200px;height:43px;line-height:43px;background:var(--teal);color:#fff;text-align:center;font-size:13.5px}
</style>
</head>
<body>

<!-- Hero -->
<div class="abs hero" role="img" aria-label="Photo of a paramotor pilot under a tan canopy and a yellow gyrocopter flying over hazy desert sky"></div>
<div class="abs hero-brand">
  <div class="mark">KRSAC</div>
  <div class="full">KESTREL RIDGE SPORTS AVIATION CLUB</div>
</div>
<div class="abs dot" style="left:579px;background:var(--magenta);border-color:var(--magenta)"></div>
<div class="abs dot" style="left:606px"></div>

<!-- Navigation -->
<nav class="abs nav">
  <a class="active" style="left:88px">Home</a>
  <a style="left:191px">About Us</a>
  <a style="left:301px">Services</a>
  <a style="left:408px">Our Team</a>
  <a style="left:526px">Events</a>
  <a style="left:619px">Contact Us</a>
  <a style="left:745px">Faq</a>
  <div class="book-now">Book Now</div>
</nav>

<!-- About -->
<div class="abs about-photo" role="img" aria-label="Photo of two smiling pilots in helmets inside a gyrocopter cockpit"></div>
<div class="abs about-title grad-text">About Us</div>
<div class="abs about-sub">WELCOME TO THE KESTREL RIDGE SPORTS AVIATION CLUB</div>
<p class="abs about-text">KRSAC represents an excitingly unique place, where aviation sports enthusiasts come together to safely enjoy the adventures life has to offer.</p>
<div class="abs btn-outline" style="left:584px;top:826px;width:125px;height:38px;line-height:34px">Read More</div>

<!-- Choose aircraft -->
<section class="abs aircraft"></section>
<h2 class="abs section-title grad-text" style="top:1047px;font-size:38px;line-height:46px">Choose your aircraft<br>to get started</h2>
<div class="abs card" style="left:88px"><div class="photo" role="img" aria-label="Photo of a white fixed wing aircraft against blue sky" style="background:radial-gradient(ellipse 110px 55px at 160px 118px,rgba(235,240,248,.95),rgba(235,240,248,0)),linear-gradient(160deg,#1f66dc,#1446b4)"></div><div class="label">Fixed wing</div></div>
<div class="abs card" style="left:440px"><div class="photo" role="img" aria-label="Photo of a yellow gyrocopter flying over the coastline" style="background:radial-gradient(ellipse 95px 45px at 165px 128px,rgba(245,205,40,.95),rgba(245,205,40,0)),radial-gradient(ellipse 200px 60px at 200px 220px,rgba(120,170,170,.8),rgba(120,170,170,0)),linear-gradient(160deg,#e4e4e0,#c8cec9 60%,#9ebcbc)"></div><div class="label">Gyrocopter</div></div>
<div class="abs card selected" style="left:792px"><div class="photo" role="img" aria-label="Photo of a paramotor pilot in flight at sunset" style="background:radial-gradient(ellipse 70px 95px at 160px 120px,rgba(40,50,100,.85),rgba(40,50,100,0)),radial-gradient(circle 105px at 160px 125px,rgba(90,80,90,.3),rgba(90,80,90,0)),linear-gradient(180deg,#9f86a8,#dca27c 55%,#f2b866)"></div><div class="label">Paramotor</div></div>
<div class="abs btn-outline" style="left:483px;top:1526px;width:234px;height:39px;line-height:35px;font-size:14px">Get an Introductory Flight</div>

<!-- Services -->
<h2 class="abs section-title grad-text" style="top:1746px;font-size:38px">Services</h2>
<div class="abs svc" style="left:200px"><svg class="icon" viewBox="0 0 56 56" role="img" aria-label="Skydive icon"><circle cx="28" cy="28" r="20" fill="none" stroke="#fff" stroke-width="2"/><path d="M18 28h20M28 18v20" stroke="#fff" stroke-width="2"/></svg><div class="name">Skydive</div><div class="toggle"><svg viewBox="0 0 34 34" width="34" height="34"><path d="M12 14l5 5 5-5" fill="none" stroke="#fff" stroke-width="2"/></svg></div></div>
<div class="abs svc" style="left:406px"><svg class="icon" viewBox="0 0 56 56" role="img" aria-label="Flight club icon"><path d="M6 30h44M28 22v16M22 38h12" stroke="#fff" stroke-width="2" fill="none"/><ellipse cx="28" cy="30" rx="9" ry="5" fill="none" stroke="#fff" stroke-width="2"/></svg><div class="name">Flight Club</div><div class="toggle"><svg viewBox="0 0 34 34" width="34" height="34"><path d="M12 14l5 5 5-5" fill="none" stroke="#fff" stroke-width="2"/></svg></div></div>
<div class="abs svc selected" style="left:611px"><svg class="icon" viewBox="0 0 56 56" role="img" aria-label="Paramotor icon"><path d="M8 20Q28 4 48 20" fill="none" stroke="#fff" stroke-width="2"/><path d="M12 19l16 17 16-17" fill="none" stroke="#fff" stroke-width="1.5"/><circle cx="28" cy="42" r="8" fill="none" stroke="#fff" stroke-width="2"/></svg><div class="name">Paramotor</div><div class="toggle"><svg viewBox="0 0 34 34" width="34" height="34"><path d="M14 12l5 5-5 5" fill="none" stroke="#fff" stroke-width="2"/></svg></div></div>
<div class="abs svc" style="left:818px"><svg class="icon" viewBox="0 0 56 56" role="img" aria-label="Parasail icon"><circle cx="26" cy="20" r="12" fill="none" stroke="#fff" stroke-width="2"/><path d="M8 44q10-6 20 0t20 0" fill="none" stroke="#fff" stroke-width="2"/></svg><div class="name">Parasail</div><div class="toggle"><svg viewBox="0 0 34 34" width="34" height="34"><path d="M12 14l5 5 5-5" fill="none" stroke="#fff" stroke-width="2"/></svg></div></div>

<!-- Team -->
<section class="abs team"></section>
<h2 class="abs section-title grad-text" style="top:2146px;font-size:38px">Our Teams</h2>
<div class="abs member" style="left:120px;background:radial-gradient(ellipse 90px 70px at 110px 215px,rgba(235,235,235,1),rgba(235,235,235,0)),radial-gradient(ellipse 70px 95px at 110px 95px,rgba(205,160,130,.8),rgba(205,160,130,0)),linear-gradient(180deg,#f6f6f6,#e2e2e2)" role="img" aria-label="Portrait photo of team member Rowan Ellery"></div>
<div class="abs member" style="left:366px;background:radial-gradient(ellipse 75px 100px at 110px 100px,rgba(190,140,105,.75),rgba(190,140,105,0)),linear-gradient(180deg,#4c4c4c,#2a2a2a)" role="img" aria-label="Portrait photo of team member Talia Brennick"></div>
<div class="abs" style="left:406px;top:2401px;width:150px;height:24px;display:flex;gap:14px;justify-content:center">
  <span style="width:24px;height:24px;border-radius:50%;background:#fff"></span><span style="width:24px;height:24px;border-radius:50%;background:#fff"></span><span style="width:24px;height:24px;border-radius:50%;background:var(--teal)"></span><span style="width:24px;height:24px;border-radius:50%;background:#fff"></span>
</div>
<div class="abs member" style="left:613px;background:radial-gradient(ellipse 95px 115px at 100px 100px,rgba(110,65,40,.75),rgba(110,65,40,0)),linear-gradient(180deg,#f3f3f3,#dcd8d4)" role="img" aria-label="Portrait photo of team member Nora Quill Hastings"></div>
<div class="abs member" style="left:859px;background:radial-gradient(ellipse 95px 115px at 110px 100px,rgba(175,130,85,.7),rgba(175,130,85,0)),radial-gradient(ellipse 80px 50px at 110px 215px,rgba(40,40,40,.7),rgba(40,40,40,0)),linear-gradient(180deg,#efefef,#d8d4ce)" role="img" aria-label="Portrait photo of team member Livia Marcott"></div>
<div class="abs member-name" style="left:120px">Rowan Ellery</div>
<div class="abs member-name" style="left:366px;color:var(--magenta)">Talia Brennick</div>
<div class="abs member-name" style="left:613px">Nora Quill Hastings</div>
<div class="abs member-name" style="left:859px">Livia Marcott</div>
<div class="abs btn-solid" style="left:547px;top:2523px;width:106px;height:39px;line-height:39px">View All</div>

<!-- Events -->
<section class="abs events"></section>
<h2 class="abs section-title grad-text" style="top:2716px;font-size:38px">Upcoming Events</h2>

<div class="abs ev-img" style="top:2813px;background:radial-gradient(ellipse 50px 25px at 150px 18px,rgba(215,40,40,.9),rgba(215,40,40,0)),radial-gradient(ellipse 35px 25px at 70px 65px,rgba(40,35,35,.75),rgba(40,35,35,0)),radial-gradient(circle 14px at 160px 80px,rgba(255,220,140,1),rgba(255,220,140,0)),linear-gradient(180deg,#e4a27c,#d88258 70%,#b8684a)" role="img" aria-label="Photo of a paramotor trike flying at sunset"></div>
<div class="abs ev-date" style="top:2832px"><b>29</b><span>Jun</span></div>
<div class="abs ev-title" style="top:2822px">Lorem Ipsum is simply typesetting industry.</div>
<p class="abs ev-desc" style="top:2862px">Lorem Ipsum has been the industry's standard dummy text ever since the 1500s, when an unknown printer took a galley...</p>
<div class="abs ev-btn" style="top:2843px">View Event</div>

<div class="abs ev-img" style="top:2957px;background:radial-gradient(ellipse 60px 25px at 110px 55px,rgba(245,205,40,.95),rgba(245,205,40,0)),linear-gradient(180deg,#e6e6e2,#d2d6d0 60%,#a9c2c4)" role="img" aria-label="Photo of a yellow gyrocopter flying over the shoreline"></div>
<div class="abs ev-date" style="top:2976px"><b>29</b><span>Jun</span></div>
<div class="abs ev-title" style="top:2967px">Lorem Ipsum is simply typesetting industry.</div>
<p class="abs ev-desc" style="top:3007px">Lorem Ipsum has been the industry's standard dummy text ever since the 1500s, when an unknown printer took a galley...</p>
<div class="abs ev-btn active" style="top:2987px">View Event</div>

<div class="abs ev-img" style="top:3102px;background:radial-gradient(ellipse 70px 40px at 140px 45px,rgba(90,70,55,.8),rgba(90,70,55,0)),radial-gradient(ellipse 50px 40px at 60px 50px,rgba(60,60,70,.6),rgba(60,60,70,0)),linear-gradient(90deg,#a89a8c,#d2b696 60%,#9a8a7c)" role="img" aria-label="Photo of two pilots seated in an open cockpit"></div>
<div class="abs ev-date" style="top:3121px"><b>29</b><span>Jun</span></div>
<div class="abs ev-title" style="top:3112px">Lorem Ipsum is simply typesetting industry.</div>
<p class="abs ev-desc" style="top:3151px">Lorem Ipsum has been the industry's standard dummy text ever since the 1500s, when an unknown printer took a galley...</p>
<div class="abs ev-btn" style="top:3132px">View Event</div>

<div class="abs btn-outline" style="left:547px;top:3256px;width:106px;height:38px;line-height:34px;color:var(--teal-light)">View All</div>

<!-- Partners -->
<h2 class="abs section-title grad-text" style="top:3458px;font-size:38px">Our Partners</h2>
<div class="abs arrow-btn" style="left:88px;background:var(--teal)"><svg viewBox="0 0 38 38" width="38" height="38"><path d="M22 13l-6 6 6 6" fill="none" stroke="#fff" stroke-width="2"/></svg></div>
<div class="abs arrow-btn" style="left:1074px;background:var(--grad)"><svg viewBox="0 0 38 38" width="38" height="38"><path d="M16 13l6 6-6 6" fill="none" stroke="#fff" stroke-width="2"/></svg></div>
<div class="abs partner" style="left:176px"><svg viewBox="0 0 150 80" width="150" height="80" role="img" aria-label="Partner badge"><rect x="15" y="18" width="120" height="44" rx="6" fill="#e9cddd"/></svg></div>
<div class="abs vsep" style="left:389px"></div>
<div class="abs partner" style="left:428px"><svg viewBox="0 0 150 80" width="150" height="80" role="img" aria-label="Partner badge"><rect x="15" y="18" width="120" height="44" rx="6" fill="#d3e2f0"/></svg></div>
<div class="abs vsep" style="left:618px"></div>
<div class="abs partner" style="left:658px"><svg viewBox="0 0 150 80" width="150" height="80" role="img" aria-label="Partner badge"><rect x="15" y="18" width="120" height="44" rx="6" fill="#d0e4ee"/></svg></div>
<div class="abs vsep" style="left:848px"></div>
<div class="abs partner" style="left:888px"><svg viewBox="0 0 150 80" width="150" height="80" role="img" aria-label="Partner badge"><rect x="15" y="18" width="120" height="44" rx="6" fill="#ece2c4"/></svg></div>

<!-- Footer -->
<footer class="abs footer"></footer>
<div class="abs foot-head" style="left:268px;top:3784px;font-size:17px">STAY CONNECTED!</div>
<div class="abs" style="left:451px;top:3776px;width:359px;height:37px;background:#fff;border-radius:2px;font-size:13px;color:#aaa;line-height:37px;padding-left:46px">name@email.com
  <svg class="abs" style="left:14px;top:11px" width="20" height="15" viewBox="0 0 20 15"><rect x="1" y="1" width="18" height="13" fill="none" stroke="#aac4e8" stroke-width="1.5"/><path d="M1 1l9 7 9-7" fill="none" stroke="#aac4e8" stroke-width="1.5"/></svg>
</div>
<div class="abs btn-solid" style="left:819px;top:3776px;width:112px;height:37px;line-height:37px">Submit</div>

<div class="abs" style="left:125px;top:3925px;width:280px">
  <div style="font-size:40px;font-weight:800;color:var(--teal-light);line-height:1">KRSAC</div>
  <div style="font-size:10.5px;font-weight:500;color:var(--teal-light);margin-top:8px;letter-spacing:.3px;white-space:nowrap">KESTREL RIDGE SPORTS AVIATION CLUB</div>
</div>

<div class="abs foot-head" style="left:482px;top:3864px">QUICK LINK</div>
<div class="abs foot-link" style="left:482px;top:3904px;text-decoration:underline;color:var(--magenta)">Home</div>
<div class="abs foot-link" style="left:482px;top:3928px">About Us</div>
<div class="abs foot-link" style="left:482px;top:3953px">Services</div>
<div class="abs foot-link" style="left:482px;top:3977px">Our Team</div>
<div class="abs foot-link" style="left:482px;top:4003px">Events</div>
<div class="abs foot-link" style="left:611px;top:3904px">Contact Us</div>
<div class="abs foot-link" style="left:611px;top:3928px">Faq</div>
<div class="abs foot-link" style="left:611px;top:3953px">Ground School</div>
<div class="abs foot-link" style="left:611px;top:3977px">Other Sports and Activities</div>
<div class="abs foot-link" style="left:611px;top:4003px">Our Partners</div>

<div class="abs foot-head" style="left:904px;top:3864px">CONATCT INFO</div>
<svg class="abs" style="left:904px;top:3905px" width="16" height="20" viewBox="0 0 16 20"><path d="M8 1a6 6 0 0 1 6 6c0 5-6 12-6 12S2 12 2 7a6 6 0 0 1 6-6z" fill="none" stroke="var(--teal-light)" stroke-width="2"/><circle cx="8" cy="7" r="2" fill="var(--teal-light)"/></svg>
<div class="abs foot-link" style="left:932px;top:3905px">Kestrel Ridge, Marlowe Vale</div>
<svg class="abs" style="left:904px;top:3941px" width="16" height="16" viewBox="0 0 16 16"><path d="M3 1l3 3-2 2a9 9 0 0 0 6 6l2-2 3 3-2 2C7 15 1 9 1 3z" fill="var(--teal-light)"/></svg>
<div class="abs foot-link" style="left:932px;top:3940px">+44 20 5550 1827</div>
<svg class="abs" style="left:904px;top:3978px" width="16" height="12" viewBox="0 0 16 12"><rect x="1" y="1" width="14" height="10" fill="none" stroke="var(--teal-light)" stroke-width="1.5"/><path d="M1 1l7 5 7-5" fill="none" stroke="var(--teal-light)" stroke-width="1.5"/></svg>
<div class="abs foot-link" style="left:932px;top:3974px">hello@krsac-club.example</div>
<div class="abs" style="left:904px;top:4015px;display:flex;gap:24px">
  <span style="width:12px;height:12px;border-radius:50%;background:#fff"></span><span style="width:12px;height:12px;border-radius:50%;background:var(--teal-light)"></span><span style="width:12px;height:12px;border-radius:50%;background:#fff"></span><span style="width:12px;height:12px;border-radius:50%;background:#fff"></span>
</div>
<div class="abs" style="left:1126px;top:3998px;width:42px;height:42px;border-radius:50%;background:var(--teal)"><svg viewBox="0 0 42 42" width="42" height="42"><path d="M21 29V14M15 19l6-6 6 6" fill="none" stroke="#fff" stroke-width="2.5"/></svg></div>

<div class="abs copyright">Copyright © 2022 KRSAC. All Rights Reserved</div>

</body>
</html>
```